Electrical Business Card Design

New electrical business targeting my local area
Installations
Repairs
Switchboards
TV / Vistacast / Antennas
Telephone
Data Networks
Audio Visual
Licence # 518427K
ABN 58316927405
I would like some white background, black writing, red, blue & green can be used
Designer discretion to be used on layout, colour placement & any images
Reason: To give designers more time, I thought 5 days wasn't enough
Please don't just create generic business cards................include personal details e.g. business name, contact name, ph #, email. Also include the things I do, licence # & abn (refer to brief for all details)
Thanks
Reason: Would like more designs & have now committed my payment, thank you
Industry/Entity Type
Electrical
Contact Information for Business Card
Korvane Electrical Services,
Gareth Pelling,
0438 571 963,
korvaneelectrical@wexmail.net.au,
My suburb is Ryde
Look and feel

```html
<!DOCTYPE html>
<html lang="en">
<head>
<meta charset="utf-8">
<title>Korvane Electrical Services – Business Card</title>
<link rel="stylesheet" href="https://fonts.googleapis.com/css2?family=Exo+2:ital,wght@1,400&family=Open+Sans:ital,wght@0,400;0,700;1,400&display=swap">
<style>
  :root {
    --page: #eceef3;
    --indigo: #3e3f94;
    --cyan: #0aa7e8;
    --white: #ffffff;
    --ink: #2b2b2b;
    --grey: #444a52;
    --rule-grey: #8c8f94;
    --brand-blue: #3b3d92;
  }
  * { margin: 0; padding: 0; box-sizing: border-box; }
  html, body { width: 1200px; height: 1064px; overflow: hidden; background: var(--page); }
  .canvas { position: relative; width: 1200px; height: 1064px; }

  .card {
    position: absolute;
    left: 290px;
    width: 620px;
    height: 354px;
    border-radius: 20px;
    overflow: hidden;
    box-shadow: 0 6px 18px rgba(40, 44, 70, 0.18);
  }
  .card-front { top: 148px; background: var(--indigo); }
  .card-back  { top: 562px; background: var(--white); }

  .card svg.rules { position: absolute; inset: 0; width: 100%; height: 100%; }

  .brand-line {
    position: absolute;
    left: 0; right: 0; top: 92px;
    text-align: center;
    font-family: "Exo 2", sans-serif;
    font-style: italic;
    font-size: 29px;
    letter-spacing: 1.5px;
    color: var(--white);
  }

  .brand-stack {
    position: absolute;
    left: 30px; width: 270px; top: 112px;
    text-align: center;
    font-family: "Exo 2", sans-serif;
    font-style: italic;
    font-size: 27px;
    line-height: 1.3;
    letter-spacing: 1px;
    color: var(--brand-blue);
  }

  .person { position: absolute; left: 340px; top: 36px; font-family: "Open Sans", sans-serif; }
  .person-name { font-weight: 700; font-size: 18px; color: var(--ink); letter-spacing: 0.3px; }
  .person-role { font-size: 16px; color: var(--grey); margin-top: 2px; }

  .contact-list {
    position: absolute; left: 336px; top: 130px;
    list-style: none;
    font-family: "Open Sans", sans-serif;
    font-style: italic;
    font-size: 14px;
    color: var(--ink);
    white-space: nowrap;
  }
  .contact-list li { height: 25px; line-height: 25px; }

  .services {
    position: absolute; left: 16px; right: 16px; top: 301px;
    text-align: center;
    font-family: "Open Sans", sans-serif;
    font-style: italic;
    font-size: 13px;
    line-height: 18px;
    color: var(--ink);
  }
</style>
</head>
<body>
<main class="canvas">

  <section class="card card-front" aria-label="Card front">
    <svg class="rules" viewBox="0 0 620 354" aria-hidden="true">
      <line x1="0" y1="222" x2="620" y2="222" stroke="var(--cyan)" stroke-width="6"/>
      <rect x="300" y="212" width="20" height="20" fill="var(--cyan)"/>
    </svg>
    <p class="brand-line">Korvane Electrical Services</p>
  </section>

  <section class="card card-back" aria-label="Card back">
    <svg class="rules" viewBox="0 0 620 354" aria-hidden="true">
      <line x1="318" y1="24" x2="318" y2="232" stroke="var(--rule-grey)" stroke-width="3"/>
      <rect x="310" y="138" width="16" height="10" fill="var(--cyan)"/>
      <rect x="310" y="163" width="16" height="10" fill="var(--cyan)"/>
      <rect x="310" y="188" width="16" height="10" fill="var(--cyan)"/>
      <rect x="310" y="213" width="16" height="10" fill="var(--cyan)"/>
      <line x1="0" y1="288" x2="620" y2="288" stroke="var(--cyan)" stroke-width="5"/>
      <rect x="302" y="280" width="16" height="16" fill="var(--cyan)"/>
    </svg>

    <p class="brand-stack">Korvane Electrical<br>Services</p>

    <div class="person">
      <p class="person-name">GARETH PELLING</p>
      <p class="person-role">Managing Director</p>
    </div>

    <ul class="contact-list">
      <li class="contact-phone">0438 571 963</li>
      <li class="contact-email">korvaneelectrical@wexmail.net.au</li>
      <li class="contact-licence">Licence # 518427K</li>
      <li class="contact-abn">ABN 58316927405</li>
    </ul>

    <p class="services">Installations · Repairs · Switchboards · TV / Vistacast / Antennas<br>Telephone · Data Networks · Audio Visual · Ryde</p>
  </section>

</main>
</body>
</html>
```